Letterhead for a German Distribution/Manufacturing Company

We need a professional Letterhead in a unique Design.
not to playful.
The Letterhead has to show show that we are a international company with headquater in Germany.
all details like adress, Vat Tax Number, Bank Accout, Eori, email, Company number has to be on the Letterhead.
for example use: VAT TAX DE5704168 Bank Account: Norrfeld Bank IBAN DE421705238ß310482 Swift: KOLV3154802 EORI 3041296587 Company Number: HRB 61508 Adress: VOLTRINA UG Amsel Strasse 7 Postal Code 04683 City Hollbrück Country: Germany Email: info@voltrina-example.com
the design can be colored but doesnt have to be
Industry/Entity Type
Manufacturing and international distribution
Requirements
Must have
- show that we are a international company with headquater in Germany. our company infos and logo

```html
<!DOCTYPE html>
<html lang="en">
<head>
<meta charset="utf-8">
<title>VOLTRINA UG – Letterhead</title>
<link rel="stylesheet" href="https://fonts.googleapis.com/css2?family=Open+Sans:ital,wght@0,400;0,600;1,400&family=Roboto:ital,wght@0,400;0,500;1,400&display=swap">
<style>
  :root {
    --backdrop: #d9d9d9;
    --paper: #ffffff;
    --band: #3f3f3f;
    --band-text: #f2f2f2;
    --body-text: #555555;
    --footer-text: #3a3a3a;
    --signature-tone: #d6dbe6;
  }
  * { box-sizing: border-box; margin: 0; padding: 0; }
  html, body {
    width: 1200px;
    height: 1058px;
    overflow: hidden;
    background: var(--backdrop);
  }
  .letterhead {
    position: absolute;
    left: 246px;
    top: 29px;
    width: 708px;
    height: 1000px;
    background: var(--paper);
    box-shadow: 0 6px 24px rgba(0,0,0,0.18);
    font-family: "Open Sans", Arial, sans-serif;
  }
  .header-band {
    position: absolute;
    left: 0; top: 0;
    width: 100%;
    height: 78px;
    background: var(--band);
    color: var(--band-text);
    display: flex;
    align-items: center;
    padding: 0 38px 0 62px;
  }
  .brand {
    display: flex;
    align-items: center;
    gap: 10px;
    font-family: "Roboto", Arial, sans-serif;
    font-size: 27px;
    font-weight: 400;
    letter-spacing: 1px;
    color: var(--band-text);
  }
  .brand-dot {
    width: 22px; height: 22px;
    border-radius: 50%;
    background: var(--band-text);
  }
  .company-address {
    margin-left: auto;
    font-family: "Roboto", Arial, sans-serif;
    font-style: italic;
    font-size: 11.5px;
    line-height: 1.4;
    text-align: left;
  }
  .company-contact {
    margin-left: 28px;
    font-family: "Roboto", Arial, sans-serif;
    font-style: italic;
    font-size: 11.5px;
    line-height: 1.4;
    list-style: none;
  }
  .company-contact li { display: flex; align-items: center; gap: 6px; }
  .company-contact svg { width: 11px; height: 11px; fill: var(--band-text); flex: none; }

  .letter-body {
    position: absolute;
    left: 110px;
    top: 205px;
    width: 500px;
    font-size: 11.4px;
    line-height: 1.52;
    color: var(--body-text);
  }
  .salutation { margin-bottom: 14px; }
  .letter-body p.paragraph { margin-bottom: 14px; }
  .closing { margin-top: 4px; }
  .signature {
    display: block;
    margin-top: 18px;
    width: 80px;
    height: 56px;
    border-radius: 4px;
    background: linear-gradient(135deg, var(--signature-tone), #eef0f5);
  }

  .footer-details {
    position: absolute;
    left: 0;
    bottom: 56px;
    width: 100%;
    text-align: center;
    font-family: "Roboto", Arial, sans-serif;
    font-size: 11.5px;
    line-height: 1.55;
    color: var(--footer-text);
  }
  .footer-details .divider { font-weight: 500; margin: 0 4px; }
</style>
</head>
<body>
  <article class="letterhead">
    <header class="header-band">
      <div class="brand"><span class="brand-dot"></span>VOLTRINA</div>
      <address class="company-address">
        VOLTRINA UG<br>
        Amsel Strasse 7 04683<br>
        City Hollbrück Germany
      </address>
      <ul class="company-contact">
        <li><svg viewBox="0 0 24 24"><path d="M6.6 10.8a15.1 15.1 0 0 0 6.6 6.6l2.2-2.2a1 1 0 0 1 1-.25 11.4 11.4 0 0 0 3.6.57 1 1 0 0 1 1 1V20a1 1 0 0 1-1 1A17 17 0 0 1 3 4a1 1 0 0 1 1-1h3.5a1 1 0 0 1 1 1c0 1.25.2 2.450.57 3.57a1 1 0 0 1-.25 1z"/></svg>415.555.0172</li>
        <li><svg viewBox="0 0 24 24"><path d="M2 5h20v14H2z M2 5l10 8 10-8" /></svg>info@voltrina-example.com</li>
        <li><svg viewBox="0 0 24 24"><circle cx="12" cy="12" r="10"/></svg>www.voltrina-example.com</li>
      </ul>
    </header>

    <section class="letter-body">
      <p class="salutation">Dear customer,</p>
      <p class="paragraph">Lorem ipsum dolor sit amet, consectetur adipisicing elit, sed do eiusmod tempor incididunt ut labore et dolore magna aliqua. Ut enim ad minim veniam, quis nostrud exercitation ullamco laboris nisi ut aliquip ex ea commodo consequat. Duis aute irure dolor in reprehenderit in voluptate velit esse cillum dolore eu fugiat nulla pariatur. Excepteur sint occaecat cupidatat non proident, sunt in culpa qui officia deserunt mollit anim id est laborum.</p>
      <p class="paragraph">Lorem ipsum dolor sit amet, consectetur adipisicing elit, sed do eiusmod tempor incididunt ut labore et dolore magna aliqua. Ut enim ad minim veniam, quis nostrud exercitation ullamco laboris nisi ut aliquip ex ea commodo consequat. Duis aute irure dolor in reprehenderit in voluptate velit esse cillum dolore eu fugiat nulla pariatur. Excepteur sint occaecat cupidatat non proident, sunt in culpa qui officia deserunt mollit anim id est laborum.</p>
      <p class="paragraph">Lorem ipsum dolor sit amet, consectetur adipisicing elit, sed do eiusmod tempor incididunt ut labore et dolore magna aliqua. Ut enim ad minim veniam, quis nostrud exercitation ullamco laboris nisi ut aliquip ex ea commodo consequat. Duis aute irure dolor in reprehenderit in voluptate velit esse cillum dolore eu fugiat nulla pariatur. Excepteur sint occaecat cupidatat non proident, sunt in culpa qui officia deserunt mollit anim id est laborum.</p>
      <p class="paragraph">Lorem ipsum dolor sit amet, consectetur adipisicing elit, sed do eiusmod tempor incididunt ut labore et dolore magna aliqua. Ut enim ad minim veniam, quis nostrud exercitation ullamco laboris nisi ut aliquip ex ea commodo consequat. Duis aute irure dolor in reprehenderit.</p>
      <p class="closing">Yours Sincerely,</p>
      <span class="signature" role="img" aria-label="Handwritten signature"></span>
    </section>

    <footer class="footer-details">
      VAT TAX DE5704168 <span class="divider">|</span> Bank Account: Norrfeld Bank IBAN DE421705238ß310482<br>
      Swift: KOLV3154802 EORI 3041296587 <span class="divider">|</span> Company Number: HRB 61508
    </footer>
  </article>
</body>
</html>
```